Orthodontic Liaison Guild Annual Conference 2016 Flyer

We need a two page attention grabbing flyer promoting our upcoming conference in Dallas, TX at the Brackenridge Inn on August 27th and 28th 2016. The flyer should give information about the conference and what you will learn by attending and to accept registration through an Ticketvale link. Our mission is to define, educate and support the role of the dental implant coordinator. Bringing together like-minded professionals to network, practice share and define our role in the delivery of comprehensive patient care. 2 day annual conference open to Surgical implant coordinators and their surgeons

Target Market(s)

Surgical Implant Treatment Coordinators, their surgeons, and surgical team members

Industry/Entity Type

Dental

Requirements
Must have
• The ability for me to make changes.
Nice to have
• professional, eye catching,

```html
<!DOCTYPE html>
<html lang="en">
<head>
<meta charset="utf-8">
<title>Orthodontic Liaison Guild Annual Conference 2016 – Speakers</title>
<link href="https://fonts.googleapis.com/css2?family=Lato:ital,wght@0,400;0,700;0,900;1,400&family=Oswald:wght@400;500&family=Archivo+Black&display=swap" rel="stylesheet">
<style>
  :root {
    --header-blue: #1d6fb8;
    --header-stripe: #3a86c6;
    --paper: #ececec;
    --orange: #f26a21;
    --ink-grey: #555555;
    --circle-navy: #1f4f7c;
    --circle-orange: #f47b20;
    --circle-sky: #1b9ad8;
    --bar-slate: #3f4546;
    --bar-green: #0e8a6c;
    --box-blue: #2097c4;
    --box-dark: #263b42;
    --footer-green: #2ca04c;
    --white: #ffffff;
  }
  * { box-sizing: border-box; margin: 0; padding: 0; }
  html, body { width: 926px; height: 1200px; overflow: hidden; }
  body { font-family: "Lato", Arial, sans-serif; background: var(--paper); position: relative; }

  .header { position: absolute; left: 0; top: 0; width: 926px; height: 148px; background: var(--header-blue); overflow: hidden; }
  .header-stripe { position: absolute; left: 0; top: 0; }
  .header-title { position: absolute; left: 80px; top: 64px; font-family: "Lato", Arial, sans-serif; font-weight: 900; font-size: 52px; line-height: 60px; color: var(--white); }
  .header-note { position: absolute; right: 93px; top: 43px; width: 410px; text-align: right; font-weight: 900; font-size: 21px; line-height: 25px; color: var(--white); }

  .speakers { position: absolute; left: 80px; top: 181px; width: 745px; }
  .speaker { font-size: 19px; line-height: 21px; margin-bottom: 22px; }
  .speaker-name { color: var(--orange); font-weight: 700; }
  .speaker-talk { color: var(--ink-grey); font-style: italic; }

  .pricing { position: absolute; left: 126px; top: 458px; display: flex; gap: 8px; }
  .price-circle { width: 216px; height: 216px; border-radius: 50%; display: flex; align-items: center; justify-content: center; text-align: center; font-family: "Oswald", Arial, sans-serif; font-weight: 500; font-size: 28px; line-height: 29px; color: var(--white); padding: 6px 20px 0; }
  .price-circle.early { background: var(--circle-navy); }
  .price-circle.member { background: var(--circle-orange); }
  .price-circle.team { background: var(--circle-sky); }

  .feature { position: absolute; color: var(--white); font-weight: 900; font-size: 21px; line-height: 25px; display: flex; align-items: center; padding: 0 20px; }
  .feature.breakout-split { left: 93px; top: 719px; width: 737px; height: 52px; background: var(--bar-slate); }
  .feature.breakout-topics { left: 93px; top: 781px; width: 737px; height: 70px; background: var(--bar-green); padding-right: 80px; }
  .feature.panel { left: 93px; top: 863px; width: 472px; height: 110px; background: var(--box-blue); padding: 0 14px 0 20px; font-size: 20.5px; line-height: 24px; letter-spacing: -0.2px; }
  .feature.meals { left: 574px; top: 863px; width: 256px; height: 110px; background: var(--box-dark); justify-content: center; text-align: center; font-family: "Archivo Black", Arial, sans-serif; font-weight: 400; font-size: 29px; line-height: 27px; letter-spacing: -1px; }

  .footer { position: absolute; left: 0; top: 1034px; width: 926px; height: 166px; background: var(--footer-green); text-align: center; color: var(--white); padding-top: 38px; }
  .footer-text { font-weight: 900; font-size: 21px; line-height: 23px; width: 700px; margin: 0 auto; }
  .footer-link { display: block; margin-top: 5px; font-weight: 700; font-size: 16px; color: var(--white); text-decoration: underline; }
</style>
</head>
<body>
  <header class="header">
    <svg class="header-stripe" width="926" height="148" viewBox="0 0 926 148" aria-hidden="true">
      <polygon points="305,0 345,0 460,148 420,148" fill="var(--header-stripe)" opacity="0.55"/>
    </svg>
    <h1 class="header-title">SPEAKERS</h1>
    <p class="header-note">Conference open to Surgical Implant Treatment Coordinators and their surgeons</p>
  </header>

  <section class="speakers">
    <p class="speaker"><span class="speaker-name">Dr. Marlow Kesterfield, DDS, MSD, Prosthodontist - </span><span class="speaker-talk">“Healthy Implants from Start to Finish”</span></p>
    <p class="speaker"><span class="speaker-name">Delia Fairbrook, America’s Body Language Expert and contributor to Harborline Report - </span><span class="speaker-talk">“The Body Language of Effective Communication”</span></p>
    <p class="speaker"><span class="speaker-name">Dr. Howard T. Linscombe, DDS, Professor of Surgery &amp; Chief, Eastbrook University School of Medicine, Dept of OMS - </span><span class="speaker-talk">“The Effective use of rhBMP in Implant Dentistry”</span></p>
    <p class="speaker"><span class="speaker-name">Renata Colby, Professional Speaker, Author and Conversation Coach - </span><span class="speaker-talk">“Team Building, Communication, and Case Acceptance”</span></p>
  </section>

  <section class="pricing">
    <div class="price-circle early">Cost by<br>June 30th<br>$699<br>after June 30th<br>$769</div>
    <div class="price-circle member">OLG<br>member cost<br>$100 off<br>conference<br>registration</div>
    <div class="price-circle team">Multiple team<br>member<br>discount $75<br>off conference<br>registration</div>
  </section>

  <div class="feature breakout-split">Additional moderated Dr only breakout and SITC only breakout</div>
  <div class="feature breakout-topics">Breakout sessions including internet marketing, financial, communication, and utilizing an SITC</div>
  <div class="feature panel">Q&amp;A and practice sharing from a<br>Surgeon/SITC panel with both OMS and<br>Perio practices</div>
  <div class="feature meals">Breakfast<br>and Lunch<br>included</div>

  <footer class="footer">
    <p class="footer-text">Book your hotel reservation at The Brackenridge Inn $169/night room block through August 4, 2016.</p>
    <a class="footer-link" href="https://book.roomhold.com/Reserve.do?group=olgannual&amp;block=ROOMS2016">https://book.roomhold.com/Reserve.do?group=olgannual&amp;block=ROOMS2016</a>
  </footer>
</body>
</html>
```